Dunecrest Motocross Club. Sports club.

We are a family orientated Motocross Club in Abu Dhabi. We have 3 motocross tracks, Intermediate Track, Junior rack and E-track. We also have a School(Academy) and maintenance facility that caters for all motorbike services. We have a BBQ area with a 20x70 meter pool after a hot day of riding. We are busy adding a restaurant and bar in the next few weeks. We host 6 Club races in the season as well as the Sandveil Open Championship. Therefore we will need a race calendar as well as race results page. The school have a dedicated school facility with bike rental, bike show room, gear rental and small shop. We have instructors that instruct kids from 4 years old to professional riders.

Target Market(s)

Motocross riders, kids from 4 years

Industry/Entity Type

extreme sports, motorsports motocross

Coding

Coded - Design and coding required

Number of Pages Required

5+ page

Font styles to use
Sans Serif

Colors

Designer to choose colors to be used in the design.

Requirements
Must have
• User Friendly, Easy to update, Calendar , online payment, race results, academy, facilities,
Nice to have
• Just an update it has to have a calendar with sides that shows whats happening on the day. We also need at the top of page the "open hours", " a next event" button, our partners button at the bottom of page a "News Page" "testimonials" with all the necessary links, social medial, address, contact details, etc.
Should not have
• no cartoons or any clipart please just photos

```html
<!DOCTYPE html>
<html lang="en">
<head>
<meta charset="utf-8">
<title>Dunecrest Motocross Club</title>
<link href="https://fonts.googleapis.com/css2?family=Barlow+Condensed:ital,wght@0,700;1,800;1,900&family=Poppins:wght@400;500;600;700&display=swap" rel="stylesheet">
<style>
:root{
  --red:#e3161e;
  --red-dark:#b80e14;
  --black:#111111;
  --ink:#1c1c1c;
  --grey:#6b6b6b;
  --line:#e4e4e4;
  --paper:#ffffff;
  --soft:#f4f4f4;
  --navy:rgba(22,40,78,.88);
}
*{box-sizing:border-box;margin:0;padding:0}
html,body{width:1200px;height:3972px;overflow:hidden}
body{font-family:"Poppins",sans-serif;color:var(--ink);background:var(--paper);font-size:13px;line-height:1.6}
.display{font-family:"Barlow Condensed",sans-serif;font-style:italic;font-weight:900;text-transform:uppercase;letter-spacing:.5px;line-height:1}
.btn{display:inline-block;background:var(--red);color:#fff;font-family:"Poppins",sans-serif;font-weight:600;font-size:11px;text-transform:uppercase;letter-spacing:1px;padding:12px 26px;text-decoration:none;white-space:nowrap}
.btn.dark{background:var(--black)}
section,header,footer{position:relative;overflow:hidden}

/* header */
.site-header{height:96px;background:var(--paper);display:flex;align-items:center;padding:0 60px;gap:30px;border-bottom:1px solid var(--line)}
.brand{display:flex;align-items:center;gap:8px;font-family:"Poppins",sans-serif;font-weight:700;font-size:18px;color:var(--ink);text-transform:uppercase;letter-spacing:1px}
.brand .mark{width:12px;height:12px;background:var(--ink)}
.header-main{flex:1;display:flex;flex-direction:column;gap:10px}
.topline{display:flex;justify-content:space-between;font-size:11px;color:var(--grey)}
.topline .phone{display:flex;align-items:center;gap:6px;font-weight:600;color:var(--ink)}
.socials{display:flex;gap:8px}
.socials span{width:12px;height:12px;border-radius:50%;background:#999}
.nav{display:flex;align-items:center;gap:26px;font-size:11px;font-weight:600;text-transform:uppercase}
.nav a{color:var(--ink);text-decoration:none}
.nav a.active{color:var(--red)}
.nav .btn{margin-left:auto;padding:9px 20px;color:#fff}

/* hero */
.hero{height:600px;background:linear-gradient(100deg,#1e140e 0%,#3b2a1c 35%,#8a6a45 65%,#c9a574 100%);color:#fff}
.hero .photo{position:absolute;inset:0}
.hero-copy{position:absolute;left:100px;top:150px;width:560px}
.hero h1{font-size:68px;margin-bottom:24px}
.hero p{font-size:13px;color:#e6e6e6;margin-bottom:30px;width:430px}
.hero .cut{position:absolute;left:0;bottom:0;width:1200px;height:60px}

/* partners */
.partners{height:104px;background:var(--paper);display:flex;align-items:center}
.partners-tag{width:300px;height:104px;position:relative}
.partners-tag svg{position:absolute;inset:0}
.partners-tag h2{position:absolute;left:60px;top:34px;color:#fff;font-size:40px}
.partner-badges{flex:1;display:flex;gap:26px;align-items:center;padding-left:10px}
.partner-badges span{width:78px;height:32px;background:#d6d6d6;border-radius:3px}
.partners .btn{margin-right:60px}

/* about */
.about{height:400px;display:flex;padding:80px 100px 0;gap:40px}
.about-photos{width:460px;display:grid;grid-template-columns:1fr 1fr;grid-template-rows:140px 130px;gap:10px}
.about-photos div:nth-child(1){background:linear-gradient(160deg,#8fb0cf,#4d6a84)}
.about-photos div:nth-child(2){background:linear-gradient(160deg,#9aa3ab,#434b54)}
.about-photos div:nth-child(3){grid-column:1/3;background:linear-gradient(180deg,#c3ccd3,#6f7a85)}
.about-copy{flex:1;padding-top:10px}
.about-copy h2{font-size:40px;margin-bottom:16px}
.about-copy p{font-size:12px;color:var(--grey);margin-bottom:12px}

/* results + calendar */
.events{height:480px;display:flex;padding:50px 100px 0;gap:50px}
.results{width:360px}
.events h2{font-size:40px;margin-bottom:24px}
.result{display:flex;align-items:center;gap:14px;padding:14px 16px;background:var(--paper);box-shadow:0 4px 18px rgba(0,0,0,.08);margin-bottom:18px}
.avatar{width:56px;height:56px;border-radius:50%;background:linear-gradient(160deg,#b0b0b0,#5e5e5e);flex:none}
.result h3{font-size:13px;font-weight:600}
.result .place{font-size:11px;color:var(--grey)}
.result .date{display:flex;align-items:center;gap:6px;font-size:10px;color:var(--grey)}
.flag{width:16px;height:10px;background:linear-gradient(90deg,var(--red) 0 25%,transparent 25%),linear-gradient(180deg,#1a8a3c 0 33%,#fff 33% 66%,#111 66%)}
.calendar{flex:1}
.cal-card{box-shadow:0 4px 18px rgba(0,0,0,.08);padding:18px 22px}
.cal-bar{display:flex;align-items:center;gap:6px;margin-bottom:14px}
.cal-bar .tab{font-size:11px;padding:6px 14px;border:1px solid var(--line)}
.cal-bar .tab.on{background:var(--black);color:#fff;border-color:var(--black)}
.cal-bar .month{margin-left:auto;font-size:12px;font-weight:600}
.cal-bar .arrow{width:24px;height:24px;background:var(--red);display:grid;place-items:center}
table.cal{width:100%;border-collapse:collapse;font-size:12px;text-align:center}
.cal th{background:var(--soft);font-weight:600;padding:8px 0;border:1px solid var(--line)}
.cal td{padding:10px 0;border:1px solid var(--line)}
.cal td.muted{color:#bdbdbd}
.cal td.sun{color:var(--red)}
.cal td.event{background:#e9e9e9;font-weight:600}
.cal td.today{background:var(--red);color:#fff;font-weight:600}

/* club intro */
.club{height:640px;background:var(--black);color:#fff;text-align:center}
.club-copy{padding:70px 150px 0}
.club h2{font-size:50px;margin-bottom:22px}
.club p{font-size:12px;color:#c9c9c9;margin-bottom:26px;text-align:left}
.club .riders{position:absolute;left:0;bottom:0;width:1200px;height:300px;background:linear-gradient(180deg,#111 0%,#5c4a38 35%,#a98962 75%,#cfb084 100%)}

/* become partner */
.become{height:400px;background:linear-gradient(110deg,#6f88a4 0%,#9fb3c6 40%,#d8dde2 60%,#5d7a93 100%)}
.become-box{position:absolute;left:360px;top:110px;width:480px;height:180px;background:var(--navy);text-align:center;color:#fff;padding-top:36px}
.become h2{font-size:40px;margin-bottom:8px}
.become p{font-size:11px;color:#d6dce6;margin-bottom:20px}

/* news */
.news{height:480px;padding:50px 60px 0;text-align:center}
.news h2{font-size:46px;margin-bottom:34px}
.news-grid{display:grid;grid-template-columns:repeat(4,1fr);gap:24px}
.news-card .pic{height:210px;margin-bottom:18px}
.news-card:nth-child(1) .pic{background:linear-gradient(160deg,#a4c27a,#4f6b33)}
.news-card:nth-child(2) .pic{background:linear-gradient(160deg,#9bb87a,#5f5a40)}
.news-card:nth-child(3) .pic{background:linear-gradient(160deg,#c89a6e,#6a4b33)}
.news-card:nth-child(4) .pic{background:linear-gradient(160deg,#9fb5c9,#3c4c5c)}
.news-card h3{font-size:12px;font-weight:700;color:var(--red);text-transform:uppercase;line-height:1.45;margin:0 10px 10px}
.news-card .date{font-size:10px;color:var(--grey);text-transform:uppercase;letter-spacing:1px}

/* contact strip */
.strip{height:280px;display:flex}
.strip > div{flex:1;position:relative;color:#fff;padding:70px 60px 0}
.stay{background:linear-gradient(120deg,#1a1a1a,#3d3d3d 60%,#6a5a4a)}
.touch{background:linear-gradient(120deg,#2a2a30,#4d4e58 55%,#8c3a2e)}
.strip h2{font-size:42px;margin-bottom:12px}
.strip p{font-size:11px;color:#d0d0d0;margin-bottom:20px;width:300px}
.subscribe{display:flex;width:440px}
.subscribe span{flex:1;background:#fff;color:#9a9a9a;font-size:11px;padding:12px 14px}
.touch{display:flex;gap:30px}
.touch .btn{align-self:flex-start;margin-top:34px}

/* footer */
.site-footer{height:492px;background:var(--black);color:#cfcfcf;padding:70px 100px 0}
.footer-cols{display:flex;gap:60px}
.footer-about{width:300px}
.footer-about .brand{margin-bottom:20px;color:#fff}
.footer-about .brand .mark{background:#fff}
.footer-about p{font-size:11px;margin-bottom:18px}
.footer-about .socials span{background:#fff;width:14px;height:14px}
.footer-col{flex:1}
.footer-col h3{font-family:"Barlow Condensed",sans-serif;font-style:italic;font-weight:800;font-size:24px;text-transform:uppercase;color:#fff;margin-bottom:6px}
.footer-col .rule{width:40px;height:3px;background:var(--red);margin-bottom:16px}
.footer-col li{list-style:none;font-size:11px;text-transform:uppercase;margin-bottom:10px}
.copyright{position:absolute;left:0;right:0;bottom:0;height:50px;border-top:1px solid #2a2a2a;text-align:center;font-size:10px;line-height:50px;letter-spacing:1px;color:#8a8a8a}
</style>
</head>
<body>

<header class="site-header">
  <div class="brand"><span class="mark"></span>Dunecrest</div>
  <div class="header-main">
    <div class="topline">
      <span class="phone">
        <svg width="12" height="12" viewBox="0 0 24 24"><path fill="#e3161e" d="M6.6 10.8a15 15 0 0 0 6.6 6.6l2.2-2.2a1 1 0 0 1 1-.25 11.4 11.4 0 0 0 3.6.57 1 1 0 0 1 1 1V20a1 1 0 0 1-1 1A17 17 0 0 1 3 4a1 1 0 0 1 1-1h3.5a1 1 0 0 1 1 1c0 1.250.2 2.45.57 3.57a1 1 0 0 1-.25 1z"/></svg>
        (055) 010 4417
      </span>
      <span class="socials"><span></span><span></span><span></span><span></span></span>
    </div>
    <nav class="nav">
      <a href="#" class="active">Home</a>
      <a href="#">School</a>
      <a href="#">Motocross Club</a>
      <a href="#">Safety Course</a>
      <a href="#">Motocross Enduro</a>
      <a href="#">Contact</a>
      <a href="#" class="btn">Login / Register</a>
    </nav>
  </div>
</header>

<section class="hero">
  <div class="photo" role="img" aria-label="Motocross rider jumping over a sandy dirt track with dust spraying"></div>
  <div class="hero-copy">
    <h1 class="display">Off-Road<br>Training School</h1>
    <p>Our trails are all laid and shaped by the heroes of nature with a few finishing touches from our team. We know and believe that the natural trail is a far better teacher than any artificially created obstacle course.</p>
    <a href="#" class="btn">Motocross Club</a>
  </div>
  <svg class="cut" viewBox="0 0 1200 60" preserveAspectRatio="none">
    <polygon points="0,60 0,30 520,60" fill="#e3161e"/>
    <polygon points="0,60 1200,10 1200,60" fill="#ffffff"/>
  </svg>
</section>

<section class="partners">
  <div class="partners-tag">
    <svg viewBox="0 0 300 104" preserveAspectRatio="none"><polygon points="0,0 300,0 250,104 0,104" fill="#e3161e"/><polygon points="255,104 305,0 300,0 250,104" fill="#111"/></svg>
    <h2 class="display">Partners</h2>
  </div>
  <div class="partner-badges" role="img" aria-label="Partner badges">
    <span></span><span></span><span></span><span></span><span></span><span></span><span></span>
  </div>
  <a href="#" class="btn dark">View All</a>
</section>

<section class="about">
  <div class="about-photos">
    <div role="img" aria-label="Club members standing together at an event"></div>
    <div role="img" aria-label="Maintenance workshop interior"></div>
    <div role="img" aria-label="Riders and staff at the clubhouse"></div>
  </div>
  <div class="about-copy">
    <h2 class="display">Read about Dunecrest Motocross</h2>
    <p>Welcome! Our racing academy teaches safe motorcycle riding skills to beginner and advanced riders on all types of bikes. We believe that the more knowledge you have, the better decisions you'll make and the safer you'll be. Our goal is to help you make quality decisions in all your riding endeavours, regardless of whether you're a new rider or an experienced one. Our riding academy is where to improve your motorcycle skills.</p>
    <p>Our racing academy is led by instructors who are eager to share their know-how from the Sandveil Open Championship, most recently in the pro class.</p>
    <a href="#" class="btn">Read More</a>
  </div>
</section>

<section class="events">
  <div class="results">
    <h2 class="display">Race Results</h2>
    <div class="result">
      <div class="avatar" role="img" aria-label="Rider portrait"></div>
      <div>
        <h3>Darren Holt</h3>
        <div class="place">Sharjah, United Arab Emirates</div>
        <div class="date"><span class="flag"></span>05-06</div>
      </div>
    </div>
    <div class="result">
      <div class="avatar" role="img" aria-label="Rider portrait"></div>
      <div>
        <h3>T.K. Marlow</h3>
        <div class="place">Sharjah, United Arab Emirates</div>
        <div class="date"><span class="flag"></span>04-05</div>
      </div>
    </div>
    <div class="result">
      <div class="avatar" role="img" aria-label="Rider portrait"></div>
      <div>
        <h3>Ren Okada</h3>
        <div class="place">Ajman, United Arab Emirates</div>
        <div class="date"><span class="flag"></span>08-05</div>
      </div>
    </div>
  </div>
  <div class="calendar">
    <h2 class="display">Calendar</h2>
    <div class="cal-card">
      <div class="cal-bar">
        <span class="tab on">Month</span><span class="tab">Week</span><span class="tab">Day</span>
        <span class="month">May 2022</span>
        <span class="arrow"><svg width="10" height="10" viewBox="0 0 10 10"><path d="M7 1 3 5l4 4" stroke="#fff" stroke-width="2" fill="none"/></svg></span>
        <span class="arrow"><svg width="10" height="10" viewBox="0 0 10 10"><path d="M3 1l4 4-4 4" stroke="#fff" stroke-width="2" fill="none"/></svg></span>
      </div>
      <table class="cal">
        <tr><th>Mon</th><th>Tue</th><th>Wed</th><th>Thu</th><th>Fri</th><th>Sat</th><th>Sun</th></tr>
        <tr><td class="muted">25</td><td class="muted">26</td><td class="muted">27</td><td class="muted">28</td><td class="muted">29</td><td class="muted">30</td><td class="sun">1</td></tr>
        <tr><td>2</td><td>3</td><td>4</td><td>5</td><td>6</td><td>7</td><td class="today">8</td></tr>
        <tr><td>9</td><td class="event">10</td><td>11</td><td>12</td><td>13</td><td>14</td><td class="sun">15</td></tr>
        <tr><td>16</td><td>17</td><td>18</td><td>19</td><td>20</td><td>21</td><td class="sun">22</td></tr>
        <tr><td>23</td><td>24</td><td>25</td><td>26</td><td>27</td><td>28</td><td class="sun">29</td></tr>
        <tr><td>30</td><td>31</td><td class="muted">1</td><td class="muted">2</td><td class="muted">3</td><td class="muted">4</td><td class="muted">5</td></tr>
      </table>
    </div>
  </div>
</section>

<section class="club">
  <div class="club-copy">
    <h2 class="display">Dunecrest — We live motocross, enduro and<br>off-road motorcycling</h2>
    <p>Approximately 70% of our course participants don't have any motocross or motorcycle experience. But after just one day they normally understand the basics of motocross riding and can set off on a track. In our motocross courses we categorise the participants in different skill levels so that experienced riders can take on harder obstacles while novices learn riding techniques at a relaxed pace. When signing up, you can also select a track that suits yourself. A full field to learn riding basics and more technical tracks with jumps. So, everyone can put together their optimal skill-building ride for motocross.</p>
    <a href="#" class="btn">Learn More</a>
  </div>
  <div class="riders" role="img" aria-label="Pack of motocross riders racing off the start line in dust"></div>
</section>

<section class="become" role="img" aria-label="Rider on a motocross bike in front of a blue sky">
  <div class="become-box">
    <h2 class="display">Become our partner</h2>
    <p>Put your brand where our riders and fans can see it, all season long.</p>
    <a href="#" class="btn">Get Started</a>
  </div>
</section>

<section class="news">
  <h2 class="display">Latest News Articles</h2>
  <div class="news-grid">
    <article class="news-card">
      <div class="pic" role="img" aria-label="Rider cornering on a grass track"></div>
      <h3>Motocross requirements and riding techniques in detail: things about motocross in general that are worth knowing</h3>
      <div class="date">Jan 17th</div>
    </article>
    <article class="news-card">
      <div class="pic" role="img" aria-label="Female rider on a motocross track"></div>
      <h3>Women are also riding motocross at Dunecrest. With our personal MX coach, you learn to ride motocross from the start</h3>
      <div class="date">Jan 17th</div>
    </article>
    <article class="news-card">
      <div class="pic" role="img" aria-label="Young rider training with an instructor"></div>
      <h3>Extensive, individual motocross instruction for children from 5 years of age with experienced professionals</h3>
      <div class="date">Feb 17th</div>
    </article>
    <article class="news-card">
      <div class="pic" role="img" aria-label="Enduro rider in a mountain landscape"></div>
      <h3>Riding enduro in Switzerland and Europe training in different groups for beginners as well as intermediates.</h3>
      <div class="date">March 18th</div>
    </article>
  </div>
</section>

<section class="strip">
  <div class="stay" role="img" aria-label="Riders gathered at the paddock">
    <h2 class="display">Stay updated</h2>
    <p>Get race news, training days and club events straight to your inbox.</p>
    <div class="subscribe"><span>Enter your email</span><a href="#" class="btn">Subscribe Now</a></div>
  </div>
  <div class="touch" role="img" aria-label="Rider in racing gear beside a bike">
    <div>
      <h2 class="display">Get in touch</h2>
      <p>For safety reasons, you must have a motocross racing licence for race practice or join at least one Dunecrest academy session.</p>
    </div>
    <a href="#" class="btn">Contact Us</a>
  </div>
</section>

<footer class="site-footer">
  <div class="footer-cols">
    <div class="footer-about">
      <div class="brand"><span class="mark"></span>Dunecrest</div>
      <p>Are you looking for an extraordinary motocross event? You want to feel the desert sand under the wheels and the thrill of every jump? Be part of our club family!</p>
      <div class="socials"><span></span><span></span><span></span></div>
    </div>
    <div class="footer-col">
      <h3>Support</h3><div class="rule"></div>
      <ul><li>Home</li><li>School</li><li>Motocross Club</li><li>Safety Course</li><li>Motocross Enduro</li><li>Contact</li></ul>
    </div>
    <div class="footer-col">
      <h3>Features</h3><div class="rule"></div>
      <ul><li>News</li><li>Events</li><li>Technology</li><li>Terms &amp; Merch</li><li>Registration</li><li>Find a Retailer</li></ul>
    </div>
    <div class="footer-col">
      <h3>Company</h3><div class="rule"></div>
      <ul><li>About Us</li><li>Members Area</li><li>Privacy</li><li>Testimonials</li><li>Recall Information</li><li>Global Website</li></ul>
    </div>
  </div>
  <div class="copyright">©2022 DUNECREST MOTOCROSS. ALL RIGHTS RESERVED</div>
</footer>

</body>
</html>
```